Criação de Papelaria Profissional para Beleza
A empresa queria:
" Atendemos clientes adultos masculino, feminino, adolescentes para tratamentos estéticos diversos como acne, rejuvenescimento facial, redução de medidas faciais e corporais, depilação, tratamento de celulite, estrias, medicina capilar, laser, cicatrizes, manchas, melasma, pequenos vasos, poros dilatados, limpeza de pele "

```html
<!DOCTYPE html>
<html lang="pt-BR">
<head>
<meta charset="utf-8">
<title>Lumera Clínica Estética — Envelopes</title>
<link href="https://fonts.googleapis.com/css2?family=Montserrat:wght@400;500&display=swap" rel="stylesheet">
<style>
  :root {
    --bg: #e7e9ea;
    --teal: #1fc1bb;
    --teal-deep: #14a7a2;
    --teal-soft: #3fcdc8;
    --navy: #14284a;
    --white: #ffffff;
    --ink: #1c3a5c;
    --mist: #f1f3f4;
  }
  * { box-sizing: border-box; margin: 0; padding: 0; }
  html, body { width: 1200px; height: 1200px; overflow: hidden; }
  body {
    background: var(--bg);
    font-family: "Montserrat", sans-serif;
    display: flex;
    flex-direction: column;
    align-items: center;
    justify-content: center;
    gap: 80px;
  }
  .envelope {
    position: relative;
    width: 960px;
    height: 480px;
    overflow: hidden;
    box-shadow: 0 12px 30px rgba(20, 40, 74, 0.18);
  }

  /* Corner accent area */
  .corner-accent {
    position: absolute;
    right: 0;
    bottom: 0;
    width: 420px;
    height: 220px;
  }
  .envelope--front .corner-accent {
    bottom: 40px;
    background: radial-gradient(ellipse at 100% 100%, var(--mist) 0%, rgba(241, 243, 244, 0) 70%);
  }
  .envelope--back .corner-accent {
    background: radial-gradient(ellipse at 100% 100%, var(--teal-soft) 0%, rgba(63, 205, 200, 0) 70%);
  }

  /* Front */
  .envelope--front { background: var(--white); }
  .envelope--front .band {
    position: absolute; left: 0; right: 0; bottom: 0; height: 40px;
    background: var(--teal);
    border-top: 5px solid var(--navy);
  }
  .brand {
    position: absolute;
    display: flex; flex-direction: column;
  }
  .brand__name {
    font-weight: 500;
    font-size: 52px;
    letter-spacing: 6px;
    line-height: 1;
  }
  .brand__tagline {
    font-weight: 400;
    font-size: 15px;
    letter-spacing: 7px;
    text-transform: uppercase;
    margin-top: 10px;
  }
  .envelope--front .brand { left: 70px; top: 60px; color: var(--ink); }
  .envelope--front .brand__tagline { color: var(--teal-deep); }

  /* Back */
  .envelope--back { background: var(--teal); }
  .envelope--back .flap {
    position: absolute; left: 0; top: 0; width: 100%; height: 150px;
  }
  .envelope--back .brand {
    left: 0; right: 0; top: 178px;
    align-items: center;
    color: var(--white);
  }
  .contact {
    position: absolute; left: 60px; right: 60px; bottom: 60px;
    display: flex; justify-content: space-between;
    list-style: none;
    color: var(--white);
    font-size: 14px;
  }
  .contact__item { display: flex; align-items: center; gap: 10px; white-space: nowrap; }
  .contact__icon {
    width: 24px; height: 24px; border-radius: 50%;
    border: 1.5px solid var(--white);
    display: flex; align-items: center; justify-content: center;
  }
  .contact__icon svg { width: 12px; height: 12px; }
</style>
</head>
<body>

  <section class="envelope envelope--front">
    <div class="corner-accent" role="img" aria-label="Faixa decorativa suave no canto inferior direito"></div>
    <div class="brand">
      <span class="brand__name">LUMERA</span>
      <span class="brand__tagline">Clínica Estética</span>
    </div>
    <div class="band"></div>
  </section>

  <section class="envelope envelope--back">
    <svg class="flap" viewBox="0 0 960 150" preserveAspectRatio="none" aria-hidden="true">
      <path d="M0 0 H960 V70 Q960 150 860 150 H100 Q0 150 0 70 Z" fill="var(--navy)"/>
    </svg>
    <div class="corner-accent" role="img" aria-label="Faixa decorativa suave no canto inferior direito"></div>
    <div class="brand">
      <span class="brand__name">LUMERA</span>
      <span class="brand__tagline">Clínica Estética</span>
    </div>
    <ul class="contact">
      <li class="contact__item">
        <span class="contact__icon"><svg viewBox="0 0 12 12"><path d="M6 1a3.5 3.5 0 0 0-3.5 3.5C2.5 7.5 6 11 6 11s3.5-3.5 3.5-6.5A3.5 3.5 0 0 0 6 1z" fill="#fff"/></svg></span>
        Rua das Flores, 120
      </li>
      <li class="contact__item">
        <span class="contact__icon"><svg viewBox="0 0 12 12"><path d="M2 1.5h2.5l1 2.5-1.5 1a6 6 0 0 0 3 3l1-1.5 2.5 1V10.5A1 1 0 0 1 9.5 11 8.5 8.5 0 0 1 1 2.5 1 1 0 0 1 2 1.5z" fill="#fff"/></svg></span>
        (11) 4000-1234
      </li>
      <li class="contact__item">
        <span class="contact__icon"><svg viewBox="0 0 12 12"><rect x="1" y="2.5" width="10" height="7" fill="none" stroke="#fff" stroke-width="1.2"/><path d="M1 2.5l5 4 5-4" fill="none" stroke="#fff" stroke-width="1.2"/></svg></span>
        contato@lumera.com
      </li>
      <li class="contact__item">
        <span class="contact__icon"><svg viewBox="0 0 12 12"><circle cx="6" cy="6" r="4.8" fill="none" stroke="#fff" stroke-width="1.1"/><path d="M1.2 6h9.6M6 1.2c2 2.5 2 7.1 0 9.6M6 1.2c-2 2.5-2 7.1 0 9.6" fill="none" stroke="#fff" stroke-width="1"/></svg></span>
        www.lumera.com
      </li>
    </ul>
  </section>

</body>
</html>
```